8 1/2 x 8 1/2 Social Media Design Ad - Commercial Loan Originator

Wanted
Commercial Loan Originators

* No Licensing Required
* Lend Nationwide with few exceptions
* Competitive Compensation
* You find the Investors and we handle the rest!!!

PRODUCTS
* Debt Service Coverage Loans (DSCR)
* Fix & Flip Financing
* Ground Up Construction
* Bridge Loans
* Portfolio Loans
And many more.....

Call (800) 416-9027 x24 for more information

Brightwater Lending Partners, Inc.
7200 Marlowe Lane, Brookhaven Falls, MD 20990
NMLS #318762

```html
<!DOCTYPE html>
<html lang="en">
<head>
<meta charset="utf-8">
<title>Commercial Loan Originators Wanted</title>
<link href="https://fonts.googleapis.com/css2?family=Lexend:wght@500;600&family=Poppins:wght@500;600;700&display=swap" rel="stylesheet">
<style>
  :root {
    --stage: #3d3d3d;
    --paper: #efefef;
    --paper-shade: #e4e4e4;
    --brand-blue: #0561a8;
    --brand-gold: #b09f30;
    --ink: #141414;
    --white: #ffffff;
  }
  * { margin: 0; padding: 0; box-sizing: border-box; }
  html, body { width: 1200px; height: 1196px; overflow: hidden; background: var(--stage); }
  .ad {
    position: absolute; left: 149px; top: 147px; width: 903px; height: 903px;
    background: linear-gradient(135deg, #f3f3f3 0%, var(--paper) 45%, var(--paper-shade) 100%);
    overflow: hidden; font-family: "Poppins", sans-serif; color: var(--ink);
  }
  .side-band { position: absolute; left: 714px; top: 0; width: 189px; height: 100%; background: var(--brand-blue); }
  .headline {
    position: absolute; left: 46px; top: 52px;
    font-family: "Lexend", sans-serif; font-weight: 600; font-size: 64px; line-height: 56px;
    text-transform: uppercase; white-space: nowrap;
  }
  .headline span { display: block; }
  .headline .blue { color: var(--brand-blue); }
  .headline .gold { color: var(--brand-gold); }
  .headline .wanted { letter-spacing: -0.5px; }
  .headline .commercial { letter-spacing: -2px; }
  .headline .loan { letter-spacing: -1px; }
  .headline .originators { letter-spacing: -4px; }
  .checklist { position: absolute; left: 46px; list-style: none; }
  .checklist li {
    display: flex; align-items: center; gap: 5px;
    font-size: 18px; font-weight: 500; height: 29px; white-space: nowrap;
  }
  .checklist svg { width: 16px; height: 16px; flex: none; }
  .benefits { top: 319px; }
  .products-title {
    position: absolute; left: 46px; top: 456px;
    color: var(--brand-blue); font-weight: 700; font-size: 20px; letter-spacing: 0.3px;
  }
  .products { top: 485px; }
  .call-band {
    position: absolute; left: 0; top: 665px; width: 578px; height: 90px;
    background: var(--brand-gold); color: var(--white);
    padding: 9px 0 0 46px; font-weight: 700; font-size: 36px; line-height: 38px;
    text-transform: uppercase; white-space: nowrap;
  }
  .brand-mark {
    position: absolute; left: 46px; top: 796px; display: flex; align-items: center; gap: 8px;
    color: var(--brand-blue); font-weight: 700; font-size: 15px; line-height: 18px; width: 145px;
  }
  .brand-mark .dot { width: 14px; height: 14px; border-radius: 50%; background: var(--brand-gold); flex: none; }
  .company {
    position: absolute; left: 200px; top: 789px; font-size: 19px; font-weight: 500; line-height: 24px;
    font-style: normal; white-space: nowrap;
  }
  .company .name { font-weight: 600; }
  .photo {
    position: absolute; left: 584px; width: 272px; height: 184px; border: 3px solid var(--white);
  }
  .photo-meeting { top: 55px; background: linear-gradient(120deg, #8a6a52, #e6e2de 55%, #3a3230); }
  .photo-kitchen { top: 258px; background: linear-gradient(110deg, #c79a6e, #efe6d6 55%, #b8783e); }
  .photo-office { top: 462px; background: linear-gradient(120deg, #3d6c95, #d9e4ef 55%, #24384f); }
  .photo-renovation { top: 665px; background: linear-gradient(130deg, #e8e8e8, #f6f6f6 50%, #7a6a58); }
</style>
</head>
<body>
<svg width="0" height="0" style="position:absolute">
  <symbol id="tick" viewBox="0 0 16 16">
    <circle cx="8" cy="8" r="6.6" fill="none" stroke="#0561a8" stroke-width="1.8"/>
    <path d="M4.8 8.2l2.2 2.2 5.2-5.6" fill="none" stroke="#0561a8" stroke-width="2" stroke-linecap="round" stroke-linejoin="round"/>
  </symbol>
</svg>
<main class="ad">
  <div class="side-band"></div>

  <h1 class="headline">
    <span class="blue wanted">Wanted</span>
    <span class="gold commercial">Commercial</span>
    <span class="blue loan">Loan</span>
    <span class="gold originators">Originators</span>
  </h1>

  <ul class="checklist benefits">
    <li><svg><use href="#tick"/></svg>No Licensing Required</li>
    <li><svg><use href="#tick"/></svg>Lend Nationwide With Few Exceptions</li>
    <li><svg><use href="#tick"/></svg>Competitive Compensation</li>
    <li><svg><use href="#tick"/></svg>You Find The Investors And We Handle The Rest!</li>
  </ul>

  <h2 class="products-title">PRODUCTS</h2>
  <ul class="checklist products">
    <li><svg><use href="#tick"/></svg>Debt Service Coverage Loans (DSCR)</li>
    <li><svg><use href="#tick"/></svg>Fix &amp; Flip Financing</li>
    <li><svg><use href="#tick"/></svg>Ground Up Construction</li>
    <li><svg><use href="#tick"/></svg>Bridge Loans</li>
    <li><svg><use href="#tick"/></svg>Portfolio Loans</li>
  </ul>

  <div class="call-band">Call (800) 416-9027 x24<br>For More Information</div>

  <div class="brand-mark"><span class="dot"></span><span>Brightwater Lending Partners</span></div>

  <address class="company">
    <div class="name">Brightwater Lending Partners, Inc.</div>
    <div>7200 Marlowe Lane,</div>
    <div>Brookhaven Falls, MD 20990</div>
  </address>

  <div class="photo photo-meeting" role="img" aria-label="Photo of a loan officer meeting with a client at a desk"></div>
  <div class="photo photo-kitchen" role="img" aria-label="Photo of a house frame under construction blending into a finished kitchen"></div>
  <div class="photo photo-office" role="img" aria-label="Photo of a businessman reviewing a tablet at his desk"></div>
  <div class="photo photo-renovation" role="img" aria-label="Photo of a bright room under renovation with a ladder and tools"></div>
</main>
</body>
</html>
```